Northbrook Vertebral Clinic of Weldon
Spine Surgeon
Professional
Grant Pellow, DO
Board Certified, Fellowship Trained, Reconstructive and Minimally Invasive Spine Surgery
5183 W. Tamsworth Rd., Suite 204
Harlow Springs, TX 75398
unknown at this time
unknown
grantjpellow@mailvex.net
www.NorthbrookVertebralClinic.net
Board Certified, Orthopedic surgery
Fellowship Trained, Reconstructive and Minimally Invasive Spine Surgery
Clearly highlight that I am board certified and fellowship trained in spine surgery.
I am setting up a new office and do not have phone lines ect. I will be changing my email address to a business account
Treatment of:
Back and Neck Pain,
Arm and Leg Pain,
Degenerative Disc Disease of the Spine,
Spinal Stenosis,
Herniated Discs,
Scoliosis and Spinal Deformities,
Spinal Tumors and Infections,
Spinal Compression Fractures,
Worker's Compensation Injuries,
Motor Vehicle Injuries

```html
<!DOCTYPE html>
<html lang="en">
<head>
<meta charset="utf-8">
<title>Northbrook Vertebral Clinic of Weldon – Stationery</title>
<link rel="stylesheet" href="https://fonts.googleapis.com/css2?family=Arimo:wght@400;700&display=swap">
<style>
:root{
  --navy:#1b2f5b;
  --navy-deep:#13234a;
  --blue:#2b4b8c;
  --rule:#c9ccd3;
  --paper:#ffffff;
  --ink:#222;
  --bg:#ffffff;
}
*{box-sizing:border-box;margin:0;padding:0}
html,body{width:1200px;height:701px;overflow:hidden;background:var(--bg);font-family:"Arimo",Arial,sans-serif;color:var(--ink)}
.canvas{position:relative;width:1200px;height:701px}
.sheet{position:absolute;background:var(--paper);border:1px solid var(--rule);box-shadow:0 1px 3px rgba(0,0,0,.12)}

/* brand lockup */
.brand{display:flex;align-items:center;gap:8px;color:var(--navy);font-weight:700;line-height:1.1}
.brand-dot{flex:none;border-radius:50%;background:var(--navy)}

/* business card front */
.card-front{left:24px;top:67px;width:300px;height:202px}
.card-front .name-band{height:34px;background:var(--navy);color:#fff;font-weight:700;font-size:15px;display:flex;align-items:center;justify-content:center}
.card-front .credentials{font-size:6.5px;font-weight:700;text-align:center;padding:7px 10px 0;color:var(--ink)}
.card-front .brand{position:absolute;left:14px;top:78px;font-size:10px;width:120px}
.card-front .brand-dot{width:14px;height:14px}
.card-front .contact{position:absolute;left:150px;top:68px;font-size:6.5px;line-height:1.5;color:var(--blue)}
.card-front .email{position:absolute;left:150px;top:150px;font-size:6.5px;line-height:1.5;color:var(--blue)}

/* business card back */
.card-back{left:355px;top:67px;width:298px;height:202px;display:flex;align-items:center;justify-content:center}
.card-back .treatments{text-align:center;font-size:8.4px;line-height:1.32;color:var(--ink)}
.card-back .treatments h3{font-size:8.6px;font-weight:700}

/* envelope */
.envelope{left:24px;top:300px;width:629px;height:384px;border:none;box-shadow:none;background:none}
.envelope svg.flap{position:absolute;left:0;top:0}
.envelope .url-band{position:absolute;left:0;top:66px;width:629px;height:40px;background:var(--navy);color:#fff;font-size:9px;font-weight:700;display:flex;align-items:center;justify-content:center}
.envelope .body{position:absolute;left:0;top:106px;width:629px;height:278px;background:var(--paper);border:1px solid var(--rule);border-top:none}
.envelope .brand{position:absolute;left:18px;top:22px;font-size:13px;width:180px}
.envelope .brand-dot{width:18px;height:18px}
.envelope .return{position:absolute;left:18px;top:198px;font-size:6.6px;line-height:1.45;color:var(--ink)}
.envelope .return .gap{margin-top:6px}

/* letterhead */
.letterhead{left:684px;top:24px;width:492px;height:660px}
.letterhead .url-band{height:30px;background:var(--navy);color:#fff;font-size:9px;font-weight:700;display:flex;align-items:center;justify-content:center}
.letterhead .accent{height:3px;background:var(--blue);opacity:.55}
.letterhead .brand{position:absolute;left:16px;top:56px;font-size:12px;width:170px}
.letterhead .brand-dot{width:16px;height:16px}
.letterhead .contact{position:absolute;right:18px;top:58px;font-size:6px;line-height:1.45;color:var(--blue);text-align:left}
</style>
</head>
<body>
<main class="canvas">

  <section class="sheet card-front" aria-label="Business card, front">
    <div class="name-band">Grant Pellow, DO</div>
    <p class="credentials">Board Certified, Fellowship Trained, Reconstructive and Minimally Invasive Spine Surgery</p>
    <div class="brand"><span class="brand-dot"></span><span>Northbrook Vertebral Clinic of Weldon</span></div>
    <div class="contact">
      5183 W. Tamsworth Rd., Suite 204<br>Harlow Springs, TX 75398<br><br>
      Office: (000) 000-0000<br>Toll Free: (000) 000-0000<br>Cell: (000) 000-0000<br>Fax: (000) 000-0000
    </div>
    <div class="email">Email: grantjpellow@mailvex.net<br>www.NorthbrookVertebralClinic.net</div>
  </section>

  <section class="sheet card-back" aria-label="Business card, back">
    <div class="treatments">
      <h3>Treatment of:</h3>
      Back and Neck Pain,<br>Arm and Leg Pain,<br>Degenerative Disc Disease of the Spine,<br>Spinal Stenosis,<br>Herniated Discs,<br>Scoliosis and Spinal Deformities,<br>Spinal Tumors and Infections,<br>Spinal Compression Fractures,<br>Worker's Compensation Injuries,<br>Motor Vehicle Injuries
    </div>
  </section>

  <section class="sheet envelope" aria-label="Envelope">
    <svg class="flap" width="629" height="70" viewBox="0 0 629 70" aria-hidden="true">
      <path d="M0 70 V22 Q0 0 22 0 H607 Q629 0 629 22 V70 Z" fill="var(--navy-deep)"/>
      <path d="M0 70 Q314 40 629 70" fill="none" stroke="#ffffff" stroke-opacity=".25" stroke-width="2"/>
      <circle cx="314" cy="32" r="9" fill="#ffffff"/>
    </svg>
    <div class="url-band">www.NorthbrookVertebralClinic.net</div>
    <div class="body">
      <div class="brand"><span class="brand-dot"></span><span>Northbrook Vertebral Clinic of Weldon</span></div>
      <div class="return">
        5183 W. Tamsworth Rd., Suite 204<br>Harlow Springs, TX 75398
        <div class="gap">Toll Free: (000) 000-0000<br>Phone: (000) 000-0000<br>Cell: (000) 000-0000<br>Fax: (000) 000-0000</div>
      </div>
    </div>
  </section>

  <section class="sheet letterhead" aria-label="Letterhead">
    <div class="url-band">www.NorthbrookVertebralClinic.net</div>
    <div class="accent"></div>
    <div class="brand"><span class="brand-dot"></span><span>Northbrook Vertebral Clinic of Weldon</span></div>
    <div class="contact">
      5183 W. Tamsworth Rd., Suite 204<br>Harlow Springs, TX 75398<br>
      Toll Free: (000) 000-0000<br>Phone: (000) 000-0000<br>Cell: (000) 000-0000<br>Fax: (000) 000-0000
    </div>
  </section>

</main>
</body>
</html>
```